trading data display webpage

We have build a rough wireframe of the two webpages that we want to display .The two wireframes are attached as a pdf document.
there will be login page. after login , the user will see the index page. that is the first page of the wireframe.

what we are displaying is essentially spread data. we are taking the difference in prices are two places and displaying the data. some calculations are done and is shown in the grid.

below the grid we show the behaviour on a graph. we will use bubble chart. I did not find a sample, hence have thrown in a placeholder.

this is time series data ( changes daily) and hence we need to check the behaviour.

the second wire frame shows how the user will choose the source price points and the destination price points.
we are talking here of natural gas prices hence the reference to source prices and destination prices.

you need to design the page/ pages such that the end-user loves it and is easy to use. the intent here is easy to use and easy to understand.
this will be responsive webpage since the end user will check it out on a tablet or a smartphone.

so if possible tell us how the navigation bar, the button bar, etc should fall when the screen size decreases.

I have uploaded 2 files. one is the wireframe ( pdf document) and second is the logo file.

please also let us know where to place the logo.

Target Market(s)

the target market is traders and data analyst

Industry/Entity Type

Build

Colors

Designer to choose colors to be used in the design.

Requirements
Must have
• 1. design for the web.
2. but think how the design will look when the screen size decreases.
3. tell if possible what screen components to keep and what to hide.

```html
<!DOCTYPE html>
<html lang="en">
<head>
<meta charset="UTF-8">
<title>Northvale Admin – Sign in</title>
<link href="https://fonts.googleapis.com/css2?family=Oswald:wght@400;500&family=Open+Sans:wght@400&display=swap" rel="stylesheet">
<style>
  :root {
    --page-bg: #333333;
    --card-bg: #ffffff;
    --heading: #2b2b2b;
    --muted: #777777;
    --field-border: #cccccc;
    --placeholder: #999999;
    --body-text: #333333;
    --link: #3a8fd9;
    --accent: #e74c3c;
    --accent-border: #d43f2f;
    --on-dark: #ffffff;
  }
  * { box-sizing: border-box; margin: 0; padding: 0; }
  html, body {
    width: 1200px;
    height: 807px;
    overflow: hidden;
    background: var(--page-bg);
    font-family: "Open Sans", Arial, sans-serif;
  }
  .login-page {
    position: relative;
    width: 1200px;
    height: 807px;
  }
  .brand {
    position: absolute;
    top: 112px;
    left: 0;
    width: 1200px;
    text-align: center;
  }
  .brand-name {
    font-family: "Oswald", Arial, sans-serif;
    font-weight: 500;
    font-size: 46px;
    line-height: 1;
    color: var(--on-dark);
  }
  .login-card {
    position: absolute;
    left: 327px;
    top: 196px;
    width: 541px;
    height: 445px;
    background: var(--card-bg);
    border-radius: 3px;
    padding: 48px 67px 0;
  }
  .login-title {
    font-family: "Oswald", Arial, sans-serif;
    font-weight: 400;
    font-size: 29px;
    color: var(--heading);
    text-align: center;
    line-height: 1.2;
    letter-spacing: -0.2px;
  }
  .login-subtitle {
    font-family: "Oswald", Arial, sans-serif;
    font-weight: 400;
    font-size: 16.5px;
    color: var(--muted);
    text-align: center;
    margin-top: 16px;
  }
  .login-form { margin-top: 36px; }
  .field {
    display: block;
    width: 100%;
    height: 47px;
    border: 1px solid var(--field-border);
    border-radius: 4px;
    padding: 0 15px;
    font-family: "Open Sans", Arial, sans-serif;
    font-size: 16.5px;
    color: var(--body-text);
    background: var(--card-bg);
  }
  .field::placeholder { color: var(--placeholder); }
  .field + .field { margin-top: 23px; }
  .form-options {
    display: flex;
    justify-content: space-between;
    align-items: center;
    margin-top: 24px;
    height: 22px;
  }
  .remember {
    display: flex;
    align-items: center;
    gap: 9px;
    font-size: 17px;
    color: var(--body-text);
  }
  .remember input {
    width: 15px;
    height: 15px;
    margin: 0;
  }
  .forgot-link {
    font-size: 16.5px;
    color: var(--link);
    text-decoration: none;
  }
  .signin-button {
    display: flex;
    justify-content: center;
    align-items: center;
    gap: 14px;
    width: 100%;
    height: 55px;
    margin-top: 23px;
    background: var(--accent);
    border: 1px solid var(--accent-border);
    border-radius: 4px;
    font-family: "Open Sans", Arial, sans-serif;
    font-size: 21.5px;
    color: var(--on-dark);
    cursor: pointer;
  }
  .signup-prompt {
    position: absolute;
    top: 669px;
    left: 0;
    width: 1200px;
    text-align: center;
    font-size: 17px;
    color: var(--on-dark);
  }
  .signup-prompt a {
    color: var(--link);
    text-decoration: none;
    margin-left: 10px;
  }
</style>
</head>
<body>
<main class="login-page">
  <header class="brand">
    <span class="brand-name">Northvale</span>
  </header>

  <section class="login-card">
    <h1 class="login-title">Welcome back to Northvale Admin.</h1>
    <p class="login-subtitle">Please sign in to get access.</p>

    <form class="login-form">
      <input class="field" type="text" placeholder="Username">
      <input class="field" type="password" placeholder="Password">

      <div class="form-options">
        <label class="remember"><input type="checkbox"> Remember me</label>
        <a class="forgot-link" href="#">Forgot Password?</a>
      </div>

      <button class="signin-button" type="button">
        Signin
        <svg width="19" height="19" viewBox="0 0 20 20" aria-hidden="true">
          <circle cx="10" cy="10" r="9" fill="#ffffff"/>
          <path d="M8 6 L14 10 L8 14 Z" fill="#e74c3c"/>
        </svg>
      </button>
    </form>
  </section>

  <p class="signup-prompt">Don't have an account? <a href="#">Create an Account!</a></p>
</main>
</body>
</html>
```